Business Card Design

We need a new buisness card designed for a new company in Darwin
We dig trenchs and lay pipes for the communication industry,Electrical industry, Teleco industry,
We also do some concrete works as well,
And small excavation work
Industry/Entity Type
Communication
Contact Information for Business Card
Tolvani Contracting PTY LTD
Pit and Pipe installations
Trenching,Excavations, Concreting ,
civil works, unistrut soloutions ,over thirty years experiance
WHERE NOT FAZED WE WILL LAY ANYTHING
Contact Glen 0451936024 ps
(would like name to stand out somehow in another text or graphic sort of a way am also looking for some sort of slogan) will most likely be a red card with black writing

```html
<!DOCTYPE html>
<html lang="en">
<head>
<meta charset="utf-8">
<title>Tolvani Contracting – Business Card</title>
<link href="https://fonts.googleapis.com/css2?family=Exo+2:wght@300;400;700;800&display=swap" rel="stylesheet">
<style>
  :root {
    --backdrop: #d2d2d2;
    --card-red: #e01e25;
    --ink: #111111;
    --paper-white: #ffffff;
    --rule: #f07a7e;
  }
  * { box-sizing: border-box; margin: 0; padding: 0; }
  html, body {
    width: 1200px;
    height: 1000px;
    overflow: hidden;
    background: var(--backdrop);
    font-family: "Exo 2", sans-serif;
  }
  .business-card {
    position: absolute;
    left: 220px;
    top: 280px;
    width: 760px;
    height: 440px;
    background: var(--card-red);
    color: var(--ink);
  }
  .brand {
    position: absolute;
    left: 52px;
    top: 58px;
    display: flex;
    align-items: center;
    gap: 18px;
  }
  .brand-square {
    width: 64px;
    height: 64px;
    background: var(--ink);
  }
  .brand-name {
    font-weight: 700;
    font-size: 40px;
    line-height: 1;
    text-transform: uppercase;
    letter-spacing: 0.5px;
    color: var(--ink);
  }
  .brand-name .brand-sub {
    display: block;
    font-size: 17px;
    letter-spacing: 1px;
    margin-top: 4px;
  }
  .contact {
    position: absolute;
    left: 92px;
    top: 188px;
    font-weight: 300;
    font-size: 29px;
    line-height: 1.02;
    letter-spacing: 0.5px;
  }
  .experience-band {
    position: absolute;
    left: 0;
    top: 256px;
    width: 350px;
    height: 27px;
    background: var(--ink);
    color: var(--paper-white);
    font-weight: 400;
    font-size: 17px;
    line-height: 27px;
    text-align: right;
    padding-right: 10px;
  }
  .services {
    position: absolute;
    left: 410px;
    top: 138px;
    list-style: none;
    font-weight: 400;
    font-size: 15.5px;
    line-height: 1.4;
    width: 300px;
  }
  .services-rule {
    position: absolute;
    left: 420px;
    top: 216px;
    width: 340px;
    height: 1px;
    background: var(--rule);
  }
  .slogan {
    position: absolute;
    left: 0;
    right: 0;
    top: 300px;
    text-align: center;
    color: var(--paper-white);
    font-weight: 800;
    font-size: 29px;
    letter-spacing: 1px;
    text-transform: uppercase;
    padding-left: 40px;
  }
</style>
</head>
<body>
  <section class="business-card" aria-label="Tolvani Contracting business card">
    <div class="brand">
      <span class="brand-square" aria-hidden="true"></span>
      <h1 class="brand-name">Tolvani<span class="brand-sub">Contracting PTY LTD</span></h1>
    </div>

    <div class="contact">
      <p class="contact-name">GLEN</p>
      <p class="contact-phone">0451936024</p>
    </div>

    <p class="experience-band">Over Thirty Years Experiance</p>

    <ul class="services">
      <li>- Pit and Pipe installations - Trenching</li>
      <li>- Excavations &nbsp;- Concreting - Civil Works</li>
      <li>- Unistrut Soloutions</li>
    </ul>
    <span class="services-rule" aria-hidden="true"></span>

    <p class="slogan">Were not fazed we'll lay anything</p>
  </section>
</body>
</html>
```